Letterhead & logo design project

We need a letterhead for a new company called Dornavelle Ltd a firm of Chartered Accountants and Chartered Tax Advisers based in Pangbourne, Berkshire
Updates
Please include the following:
Chartered Accountants and Chartered Tax Advisers
Industry/Entity Type
It Company
Requirements
Must have
- Must have director's name at the bottom of the letterhead. Must also contain some wording at the bottom of the page to be provided by the BQRPT at a later date

```html
<!DOCTYPE html>
<html lang="en">
<head>
<meta charset="utf-8">
<title>Dornavelle Ltd — Letterhead</title>
<link rel="stylesheet" href="https://fonts.googleapis.com/css2?family=Fira+Sans:wght@500;700&family=Arimo:wght@400&display=swap">
<style>
  :root {
    --mint: #72fbdf;
    --blue: #3a74ff;
    --ink: #111111;
    --paper: #ffffff;
  }
  html, body {
    margin: 0;
    padding: 0;
    overflow: hidden;
    background: var(--paper);
  }
  .letterhead {
    position: relative;
    width: 858px;
    height: 1200px;
    overflow: hidden;
    background: var(--paper);
  }
  .band {
    position: absolute;
    left: 0;
    width: 858px;
  }
  .band--top-fill { top: 0; height: 38px; background: var(--mint); }
  .band--top-rule { top: 38px; height: 10px; background: var(--blue); }
  .band--bottom-rule { bottom: 38px; height: 10px; background: var(--blue); }
  .band--bottom-fill { bottom: 0; height: 38px; background: var(--mint); }
  .brand {
    position: absolute;
    right: 92px;
    top: 112px;
    text-align: right;
  }
  .brand__name {
    margin: 0;
    font-family: "Fira Sans", sans-serif;
    font-weight: 500;
    font-size: 45px;
    line-height: 1;
    color: var(--mint);
    white-space: nowrap;
  }
  .brand__tagline {
    margin: 14px 0 0;
    font-family: "Fira Sans", sans-serif;
    font-weight: 700;
    font-size: 12.6px;
    color: var(--ink);
    white-space: nowrap;
  }
  .signatory {
    position: absolute;
    left: 92px;
    top: 935px;
    margin: 0;
    font-family: "Fira Sans", sans-serif;
    font-weight: 700;
    font-size: 17px;
    color: var(--ink);
  }
  .footer-note {
    position: absolute;
    left: 92px;
    top: 1014px;
    width: 689px;
    margin: 0;
    font-family: "Arimo", Arial, sans-serif;
    font-size: 13.6px;
    line-height: 21px;
    text-align: justify;
    color: var(--ink);
  }
</style>
</head>
<body>
<div class="letterhead">
  <div class="band band--top-fill" aria-hidden="true"></div>
  <div class="band band--top-rule" aria-hidden="true"></div>

  <header class="brand">
    <h1 class="brand__name">Dornavelle Ltd</h1>
    <p class="brand__tagline">Chartered Accountants and Chartered Tax Advisers</p>
  </header>

  <p class="signatory">(Director)</p>

  <p class="footer-note">Lorem ipsum dolor sit amet, consectetuer adipiscing elit, sed diam nonummy nibh euismod tincidunt ut laoreet dolore magna aliquam erat volutpat. Ut wisi enim ad minim veniam, quis nostrud exerci tation ullamcorper suscipit lobortis nisl ut aliquip ex ea commodo consequat. Lorem ipsum dolor sit amet, consectetuer adipiscing elit, sed diam nonummy nibh euismod tincidunt ut laoreet.</p>

  <div class="band band--bottom-rule" aria-hidden="true"></div>
  <div class="band band--bottom-fill" aria-hidden="true"></div>
</div>
</body>
</html>
```